Up and coming Australian Systems Integrator needs a proposal template refresh

We need to update our proposal template and are looking for a fresh, modern, simple and elegant proposal template. We'd like to keep our existing logos if possible.
Quorvex is a privately owned company operating since 2006. Offices and technical staff located in Port Melbourne and Bendigo
Sustained, profitable growth year on year
Velmar strategic partner
Velmar Advanced Enterprise Network Architecture Specialisation
Velmar Advanced Security Architecture Specialisation
Velmar Advanced Collaboration Architecture Specialisation
Velmar Advanced Unified Computing Technology Specialisation
Velmar Advanced Data Centre Architecture Specialisation (in progress)
Velmar Gold Partner – Expect 2H2018
As well as being a Velmar partner we have a well established stable of other vendors such as Brandova, Teskaro, Haldenworth, ZEP, Mirvale Interactive, Dulm, TidePoint, KoMELDA Gate)
We are a top two provider of Velmar product/services in the Victorian healthcare sector.
Please feel free to use different colors and fonts as we feel the existing ones look dated.

```html
<!DOCTYPE html>
<html lang="en">
<head>
<meta charset="utf-8">
<title>Quorvex Proposal Template – Page Spread</title>
<link href="https://fonts.googleapis.com/css2?family=Open+Sans:ital,wght@0,400;0,600;0,700;1,400&display=swap" rel="stylesheet">
<style>
:root{
  --bg:#a6a6a6;
  --paper:#ffffff;
  --navy:#1b3a6b;
  --blue:#1f5fa8;
  --orange:#f47b20;
  --text:#555a60;
  --muted:#9aa0a6;
  --rule:#d7dce2;
  --tint:#dbe8f6;
  --tint2:#c6dcf2;
}
*{box-sizing:border-box;margin:0;padding:0}
html,body{width:1200px;height:1200px;overflow:hidden;background:var(--bg)}
body{font-family:"Open Sans",Arial,sans-serif;color:var(--text)}
.sheet{position:relative;width:1200px;height:1200px;background:var(--bg);overflow:hidden}
.page{position:absolute;width:216px;height:304px;background:var(--paper);box-shadow:0 1px 3px rgba(0,0,0,.25);overflow:hidden}
.c1{left:26px}.c2{left:261px}.c3{left:493px}.c4{left:726px}.c5{left:959px}
.r1{top:59px}.r2{top:395px}.r3{top:733px}

.hd{position:absolute;left:0;top:21px;display:flex;align-items:center;font-size:7px;letter-spacing:.2px;color:var(--navy);text-transform:uppercase;white-space:nowrap}
.hd::before{content:"";display:block;width:20px;height:5px;background:var(--orange);margin-right:4px}
.hd em{font-style:normal;color:var(--orange)}
.url{position:absolute;left:20px;bottom:10px;font-size:2.6px;color:var(--muted)}
.pnum{position:absolute;right:11px;bottom:0;width:5px;height:15px;background:var(--navy);border-radius:2px 2px 0 0;color:#fff;font-size:2.6px;text-align:center;padding-top:3px}

.body{position:absolute;left:20px;right:20px;top:40px}
h3{font-size:5.4px;font-weight:600;color:#333;margin:3px 0 2px}
h4{font-size:4.2px;font-weight:700;color:var(--blue);margin:2px 0 1px;line-height:5px}
p{font-size:3.2px;line-height:4.4px;margin-bottom:3px}
.it{font-style:italic;color:var(--orange);font-size:3.2px;line-height:4.2px;margin-bottom:1px}
.itg{font-style:italic;color:var(--muted);font-size:3.2px;line-height:4.2px;margin-bottom:1px}
.link{color:var(--blue)}
.ph{position:absolute;display:block}

/* cover */
.brand{position:absolute;left:0;right:0;top:36px;text-align:center}
.brand b{font-size:14px;font-weight:600;color:var(--navy);letter-spacing:1px;display:inline-flex;align-items:center;gap:5px}
.brand b i{display:inline-block;width:8px;height:8px;background:var(--orange);border-radius:50%}
.brand span{display:block;font-size:2.8px;letter-spacing:.6px;color:var(--muted);margin-top:1px}
.cover-title{position:absolute;left:27px;top:201px;font-size:11.5px;font-weight:600;line-height:17px;color:var(--navy)}
.cover-title em{font-style:normal;color:var(--orange)}
.cover-sub{position:absolute;left:28px;top:237px;font-size:4.6px;line-height:6px;color:var(--blue)}
.cover-foot{position:absolute;left:0;top:281px;display:flex;align-items:center;font-size:5px;font-weight:700;color:var(--navy)}
.cover-foot::before{content:"";display:block;width:22px;height:5px;background:var(--orange);margin-right:6px}

/* tables */
table{border-collapse:collapse;width:100%}
.ver{position:absolute;left:30px;top:38px;width:156px}
.ver td,.ver th{border:.5px solid #cfd3d8;height:10.5px;font-size:2.6px;font-weight:400;text-align:left;padding-left:2px;color:var(--blue)}
.ver th{background:#e3e6ea;height:5px}
.grid td{height:6.5px;border-right:.6px solid #fff;border-bottom:.6px solid #fff}
.grid tr:nth-child(odd) td{background:var(--tint)}
.grid tr:nth-child(even) td{background:var(--tint2)}
.grid tr:first-child td{background:var(--blue);height:4px}
.est td,.est th{font-size:2.6px;height:4.8px;padding:0 3px;border-bottom:.5px solid #fff}
.est th{background:var(--blue);color:#fff;font-weight:600}
.est td{background:var(--tint);color:var(--blue)}
.est tr.tot td{font-weight:700;background:var(--tint2)}
.est td:nth-child(n+2){text-align:center}

/* TOC */
.toc{position:absolute;left:20px;right:18px;top:40px}
.toc li{list-style:none;display:flex;gap:6px;margin-bottom:8px}
.toc .n{flex:0 0 24px;height:24px;background:var(--orange);color:#fff;font-size:13px;font-weight:600;display:flex;align-items:center;justify-content:center}
.toc h4{margin-top:0}

/* navy band page */
.navyband{position:absolute;left:0;top:0;width:216px;height:119px;background:var(--navy)}
.white h3,.white p{color:#fff}
.white .it{color:#c9d6ea}

/* orange panel */
.opanel{position:absolute;left:18px;top:0;width:97px;height:246px;background:var(--orange);padding:20px 8px 0}
.opanel .hdt{font-size:7px;color:#fff;text-transform:uppercase;margin-bottom:12px}
.opanel h3,.opanel p{color:#fff}
.opanel .it{color:#ffe0c7}

/* vision */
.vision-band{display:flex;align-items:center;gap:4px;margin-bottom:6px}
.vision-band div{flex:1;background:#4b4f55;color:#fff;font-size:3.2px;line-height:4px;padding:2px 4px}

.lightbar{height:5px;background:var(--tint);margin:4px 0}
.list-item{display:flex;gap:5px;align-items:flex-start;margin-bottom:4px}
.list-item svg{flex:0 0 16px}
.twocol{position:absolute;left:20px;right:18px;top:40px;display:flex;gap:8px}
.twocol>div{flex:1}

.back-contact{position:absolute;left:50px;top:264px;display:flex;gap:10px;align-items:flex-start}
.back-contact b{font-size:4.5px;color:var(--navy);font-weight:700;letter-spacing:.4px}
.back-contact p{font-size:2.4px;line-height:3.6px;margin:0;display:flex;align-items:center;gap:2px}
.dot{display:inline-block;width:3px;height:3px;border-radius:50%;background:var(--orange)}
</style>
</head>
<body>
<div class="sheet">

<!-- ROW 1 -->
<section class="page c1 r1">
  <div class="brand"><b><i></i>QUORVEX</b><span>NETWORK &amp; COMMUNICATIONS SOLUTIONS</span></div>
  <svg class="ph" style="left:0;top:65px" width="216" height="130" role="img" aria-label="Blue-toned photo of two hands meeting in a handshake over a digital city skyline">
    <defs><linearGradient id="cv" x1="0" y1="0" x2="1" y2="1"><stop offset="0" stop-color="#0d3d7a"/><stop offset=".5" stop-color="#3f8fd6"/><stop offset="1" stop-color="#0b2a5a"/></linearGradient></defs>
    <rect width="216" height="130" fill="url(#cv)"/>
  </svg>
  <div class="cover-title">LOREM IPSUM IS SIMPLY<br><em>DUMMY HAS BEEN</em></div>
  <div class="cover-sub">LOREM IPSUM IS SIMPLY ETIAM VESTIBULUM<br>LOREM IPSUM IS SIMPLY</div>
  <div class="cover-foot">LOREM IPSUM IS SIMPLY ETIAM VESTIBULUM</div>
</section>

<section class="page c2 r1">
  <table class="ver">
    <tr><th>Version #</th><th>Purpose / Changes</th><th>Author</th><th>Date</th></tr>
    <tr><td></td><td></td><td></td><td></td></tr><tr><td></td><td></td><td></td><td></td></tr>
    <tr><td></td><td></td><td></td><td></td></tr><tr><td></td><td></td><td></td><td></td></tr>
    <tr><td></td><td></td><td></td><td></td></tr><tr><td></td><td></td><td></td><td></td></tr>
    <tr><td></td><td></td><td></td><td></td></tr><tr><td></td><td></td><td></td><td></td></tr>
  </table>
  <div style="position:absolute;left:58px;top:250px;width:130px;border-left:.8px solid var(--orange);padding-left:3px">
    <p style="font-size:2.4px;line-height:3.3px">Copyright © 2018 Quorvex Pty Ltd<br>All Rights Reserved.<br>No part of this document may be copied or shared in any form or by any means without the prior written permission of Quorvex Pty Ltd.</p>
  </div>
</section>

<section class="page c3 r1">
  <div class="hd">Table of Contents</div>
  <ul class="toc">
    <li><span class="n">1</span><div><h4>Ledgra builds automation in stages</h4><p>System to reach full automation thanks to Ledgra AI. Ledgra AI automates tasks and allows users to communicate with it, viewing it as a trusted advisor over time for all their accounting queries.</p></div></li>
    <li><span class="n">2</span><div><h4>Ledgra builds automation in stages</h4><p>System to reach full automation thanks to Ledgra AI. Ledgra AI automates tasks and allows users to communicate with it, viewing it as a trusted advisor over time for all their accounting queries.</p></div></li>
    <li><span class="n">3</span><div><h4>Ledgra builds automation in stages</h4><p>System to reach full automation thanks to Ledgra AI. Ledgra AI automates tasks and allows users to communicate with it, viewing it as a trusted advisor over time for all their accounting queries.</p></div></li>
    <li><span class="n">4</span><div><h4>Ledgra builds automation in stages</h4><p>System to reach full automation thanks to Ledgra AI. Ledgra AI automates tasks and allows users to communicate with it, viewing it as a trusted advisor over time for all their accounting queries.</p></div></li>
  </ul>
  <span class="url">www.quorvex.example</span><span class="pnum">1</span>
</section>

<section class="page c4 r1">
  <div class="hd">Headline <em>&nbsp;Here</em></div>
  <div class="body">
    <h3>Solution</h3>
    <p class="itg">AI automated accounting</p>
    <p>Ledgra builds automation in stages on top of its current system to reach full automation. It starts by connecting to all sources of accounting data such as bank accounts, credit cards, webshops or document systems (Filebay or Nodevault). Based on these data, Ledgra AI creates bookings and generates financial reports, and features a chat-like interface that lets users talk to it as a trusted advisor.</p>
    <p class="itg">Blockchain software license or Token-as-a-License (TaaL)</p>
    <p>It is possible to create tokens on blockchain that represent software licenses, known as Token-as-a-License. Ledgra creates TaaL by using the Korvin official wallet which interacts with the Korvin blockchain. Upon purchase, the token holder is free to transfer or sell it using a secondary market built directly over the blockchain. Ledgra checks the validity of a token against the blockchain, so token holders always have access to the software. This makes distribution easier and gives the license a higher value.</p>
    <h3>Pre-ICO Token sale</h3>
    <p>To realize this vision, Ledgra is launching a pre-ICO in the form of a token sale on the Korvin blockchain. 20,000,000 tokens are available for purchase for a 30-day period. Tokens represent lifelong software licenses, and buyers of 15,000 tokens gain access to both Ledgra accounting and invoicing. Future customers will still be able to buy monthly subscriptions.</p>
    <h3>Future plans</h3>
    <p>A future ICO is planned between 18 and 24 months after the pre-ICO token sale. This offering will support a fully decentralized, privacy-focused ecosystem of applications where every participant is rewarded.</p>
  </div>
  <span class="url">www.quorvex.example</span><span class="pnum">2</span>
</section>

<section class="page c5 r1">
  <div class="navyband"></div>
  <div class="hd" style="color:#fff">Headline <em>&nbsp;Here</em></div>
  <div class="body white" style="right:112px">
    <h3>Solution</h3>
    <p class="it">AI automated accounting</p>
    <p>Ledgra builds automation in stages on top of its current system to reach full automation. Ledgra AI automates every manual task performed by the user, connecting all sources of accounting data such as bank accounts, credit cards and webshops.</p>
  </div>
  <svg class="ph" style="left:108px;top:45px" width="96" height="110" role="img" aria-label="Photo of a person in a suit working on a laptop, close-up on hands"><rect width="96" height="110" fill="#6f7d8f"/></svg>
  <svg class="ph" style="left:108px;top:170px" width="96" height="112" role="img" aria-label="Photo of a businessman in a dark suit adjusting his cuff"><rect width="96" height="112" fill="#5a5f67"/></svg>
  <div class="body" style="top:128px;right:112px">
    <h3>Solution</h3>
    <p class="itg">AI automated accounting</p>
    <p>Ledgra builds automation in stages on top of its current system to reach full automation. Ledgra AI automates every manual task performed by the user. It starts by connecting to all sources of accounting data such as bank accounts, credit cards, webshops or document systems. Based on these data, Ledgra AI creates bookings and generates financial reports. It features a chat-like interface so users can talk to it as a trusted advisor for all their accounting queries.</p>
    <p class="itg">Blockchain software license or Token-as-a-License (TaaL)</p>
    <p>It is possible to create tokens on blockchain that represent software licenses.</p>
  </div>
  <span class="url">www.quorvex.example</span><span class="pnum">2</span>
</section>

<!-- ROW 2 -->
<section class="page c1 r2">
  <div class="hd">Headline <em>&nbsp;Here</em></div>
  <div class="body">
    <h3>Implementation Estimate</h3>
    <p>The bulk of the implementation costs will be defined by discovery. Based on similar projects, we feel the effort will be between 200 and 300 hours, give or take. The wide swing reflects the loosely defined nature of both integration needs and our role in the project.</p>
    <table class="grid" style="margin-top:4px"><tr><td></td><td></td><td></td></tr><tr><td></td><td></td><td></td></tr><tr><td></td><td></td><td></td></tr><tr><td></td><td></td><td></td></tr><tr><td></td><td></td><td></td></tr><tr><td></td><td></td><td></td></tr><tr><td></td><td></td><td></td></tr></table>
    <table class="grid" style="margin-top:10px"><tr><td></td><td></td><td></td><td></td></tr><tr><td></td><td></td><td></td><td></td></tr><tr><td></td><td></td><td></td><td></td></tr><tr><td></td><td></td><td></td><td></td></tr><tr><td></td><td></td><td></td><td></td></tr><tr><td></td><td></td><td></td><td></td></tr><tr><td></td><td></td><td></td><td></td></tr></table>
    <h3 style="margin-top:22px">Implementation Estimate</h3>
    <p>The bulk of the implementation costs will be defined by discovery. Based on similar projects, we feel the effort will be between 200 and 300 hours, give or take, as it relates to integrating the sites.</p>
  </div>
  <span class="url">www.quorvex.example</span><span class="pnum">2</span>
</section>

<section class="page c2 r2">
  <div class="hd">Headline <em>&nbsp;Here</em></div>
  <div class="body">
    <h3>Implementation Estimate</h3>
    <p>The bulk of the implementation costs will be defined by discovery. Based on similar projects, we feel the effort will be between 200 and 300 hours, give or take. The wide swing reflects the loosely defined nature of both integration needs and our role in the project.</p>
    <table class="est" style="margin-top:4px">
      <tr><th>Task</th><th>Hours</th><th>Cost</th></tr>
      <tr><td>Discovery</td><td>40</td><td>$8,000</td></tr>
      <tr class="tot"><td>Phase 1</td><td></td><td></td></tr>
      <tr><td>Discovery</td><td>20-40</td><td>$8,000</td></tr>
      <tr><td>Discovery</td><td>20-40</td><td>$8,000</td></tr>
      <tr><td>Discovery</td><td>20-40</td><td>$8,000</td></tr>
      <tr class="tot"><td>Total Phase 1</td><td>80-240</td><td>$16,800-40,000</td></tr>
      <tr class="tot"><td>Phase 2</td><td></td><td></td></tr>
      <tr><td>Discovery</td><td>20-40</td><td>$8,000</td></tr>
      <tr class="tot"><td>Total Phase 2</td><td>80-240</td><td>$16,800-40,000</td></tr>
      <tr class="tot"><td>Total Estimated Implementation Cost</td><td>220-480</td><td>$44,000-96,000</td></tr>
    </table>
    <h3 style="margin-top:8px">Project Timeline</h3>
    <p>Based on the information we have at our disposal, the launch date leaves room for a realistic schedule. We recommend running discovery before committing to a build plan, with the full phase taking between 7 and 12 weeks.</p>
    <table class="est">
      <tr><th>Task</th><th>Weeks to Complete</th></tr>
      <tr><td>Discovery</td><td>1-2</td></tr>
      <tr><td>Phase 1</td><td>6-10</td></tr>
      <tr><td>Phase 2</td><td>8-12</td></tr>
      <tr class="tot"><td>Total Number of Weeks</td><td></td></tr>
    </table>
  </div>
  <span class="url">www.quorvex.example</span><span class="pnum">2</span>
</section>

<section class="page c3 r2">
  <div class="hd">Vision</div>
  <div class="body">
    <div class="vision-band">
      <svg width="13" height="13" viewBox="0 0 13 13"><circle cx="6.5" cy="6.5" r="6" fill="var(--navy)"/><circle cx="6.5" cy="6.5" r="4" fill="none" stroke="#fff" stroke-width=".8"/><circle cx="6.5" cy="6.5" r="1.8" fill="#fff"/><path d="M6.5 6.5 L11 2" stroke="var(--orange)" stroke-width="1"/></svg>
      <div>Ledgra's mission is to help and support the self-employed and small business owners with their administrative tasks so they can focus on what matters — their business.</div>
    </div>
    <p>Administrative tasks are cumbersome, time-consuming and often prevent small owners from focusing their time and energy on their business. They can also be extremely stressful for those attempting these tasks for the first time.</p>
    <p>At Ledgra, we envisage accounting for the self-employed and small business owners as being <span class="link">automated and decentralized.</span></p>
    <p>Accounting can and should be done automatically. By connecting to all sources of accounting data such as bank accounts, payment systems, e-commerce websites and invoicing systems, Ledgra AI completes these tasks, which would take hours to do manually. Bookings are created automatically, and financial statements are available within a couple of clicks.</p>
    <p>What may seem like a pipedream to millions of self-employed people who struggle with their admin is already a reality. Now is the time to join Ledgra on its mission to transform bookkeeping.</p>
    <h3>The Ledgra model</h3>
    <p>Ledgra is based on an innovative license model that uses Token-as-a-License (TaaL). The token represents lifelong software licenses for Ledgra solutions. The pre-ICO token sale will enable Ledgra to complete its development of fully automatic bookkeeping.</p>
    <p>The pre-ICO token sale will also pave the way for a future ICO. Ledgra will launch accounting on the blockchain and ensure your accounting data is comprehensive and private, available everywhere within your preferred apps.</p>
    <p>Ledgra supports strong data ownership laws that protect individuals and ensure they have full ownership of their data. To find out more about the Ledgra AI project, please register with your email at <span class="link">www.ledgra.example</span></p>
  </div>
  <span class="url">www.quorvex.example</span><span class="pnum">2</span>
</section>

<section class="page c4 r2">
  <svg class="ph" style="left:0;top:160px" width="216" height="144" role="img" aria-label="Overhead photo of a team meeting around a table with laptops and papers"><rect width="216" height="144" fill="#b58a62"/></svg>
  <div class="opanel">
    <div class="hdt">Headline Here</div>
    <h3>Solution</h3>
    <p class="it">AI automated accounting</p>
    <p>Ledgra builds automation in stages on top of its current system to reach full automation thanks to Ledgra AI. It starts by connecting to all sources of accounting data such as bank accounts, credit cards, webshops or document systems. Based on these data, Ledgra AI creates bookings and generates financial reports, and features a chat-like interface that lets users talk to it as a trusted advisor over time.</p>
    <p class="it">Blockchain software license or Token-as-a-License (TaaL)</p>
    <p>It is possible to create tokens on blockchain that represent software licenses, also known as Token-as-a-License. Ledgra creates TaaL using the Korvin official wallet. Upon purchase, the token holder is free to transfer or sell it on a secondary market built over the blockchain, and Ledgra checks each token's validity.</p>
  </div>
  <span class="pnum">2</span>
</section>

<section class="page c5 r2">
  <div class="hd">Headline <em>&nbsp;Here</em></div>
  <svg class="ph" style="left:20px;top:40px" width="95" height="116" role="img" aria-label="Photo of a businessman in a suit working at a laptop"><rect width="95" height="116" fill="#2c3e5c"/></svg>
  <svg class="ph" style="left:20px;top:172px" width="95" height="116" role="img" aria-label="Photo of a businessman in a dark suit seen from the side"><rect width="95" height="116" fill="#4a4f58"/></svg>
  <div class="body" style="left:123px;right:16px">
    <h4 style="font-size:4.6px">Ledgra's mission is to help and support the self-employed and small business owners with their administrative tasks so they can focus on what matters – their business.</h4>
    <p style="margin-top:3px">Administrative tasks are cumbersome, time-consuming and often prevent small owners from focusing their time and energy on their business. They can also be extremely stressful for those attempting these tasks for the first time.</p>
    <p>At Ledgra, we envisage accounting for the self-employed and small business owners as being <span class="link">automated and decentralized.</span></p>
    <p>Accounting can and should be done automatically. By connecting to all sources of accounting data such as bank accounts, payment systems, e-commerce websites and invoicing systems, Ledgra AI completes these tasks, which would take hours to do manually. Bookings are created automatically and financial statements are available within a couple of clicks.</p>
    <p>What may seem like a pipedream to millions of self-employed people is already a reality.</p>
    <h3>The Ledgra model</h3>
    <p>Ledgra is based on an innovative license model that uses Token-as-a-License (TaaL). The token represents lifelong software licenses for Ledgra solutions, and the pre-ICO sale will enable Ledgra to deliver fully automatic bookkeeping.</p>
  </div>
  <span class="url">www.quorvex.example</span><span class="pnum">1</span>
</section>

<!-- ROW 3 -->
<section class="page c1 r3">
  <div class="hd">Headline <em>&nbsp;Here</em></div>
  <svg class="ph" style="left:20px;top:38px" width="176" height="76" role="img" aria-label="Overhead photo of colleagues collaborating around a table with papers and laptops"><rect width="176" height="76" fill="#c4906a"/></svg>
  <div class="body" style="top:118px">
    <h4 style="font-size:4.8px">Ledgra's mission is to help and support the self-employed and small business owners with their</h4>
    <p style="margin-top:2px">Administrative tasks are cumbersome, time-consuming and often prevent small owners from focusing their time and energy on their business. They can also be extremely stressful for those attempting these tasks for the first time.</p>
    <p>At Ledgra, we envisage accounting for the self-employed and small business owners as being <span class="link">automated and decentralized</span></p>
    <div class="lightbar" style="margin-top:8px"></div>
    <div class="lightbar"></div>
    <div class="lightbar"></div>
    <div class="lightbar"></div>
    <p style="margin-top:4px">Ledgra is based on an innovative license model that uses Token-as-a-License (TaaL). The token represents lifelong software licenses for Ledgra solutions, and the pre-ICO sale will enable Ledgra to deliver fully automatic bookkeeping.</p>
    <p>With leading edge business data access to ensure you have the best available data at your fingertips.</p>
  </div>
  <span class="url">www.quorvex.example</span><span class="pnum">2</span>
</section>

<section class="page c2 r3">
  <div class="hd">Headline <em>&nbsp;Here</em></div>
  <div class="body">
    <p class="itg">AI automated accounting</p>
    <p>Ledgra builds automation in stages on top of its current system to reach full automation thanks to Ledgra AI. Ledgra AI automates every manual task performed by the user. It starts by connecting to all sources of accounting data such as bank accounts, credit cards.</p>
    <svg width="176" height="126" viewBox="0 0 176 126" style="margin:2px 0 4px">
      <g font-family="Open Sans, sans-serif" font-size="3" fill="#333" font-weight="600">
        <text x="0" y="5">Lorem Ipsum</text>
        <text x="42" y="5">Week 1</text><text x="64" y="5">Week 1</text><text x="86" y="5">Week 1</text><text x="108" y="5">Week 1</text><text x="130" y="5">Week 1</text><text x="152" y="5">Week 1</text>
      </g>
      <line x1="0" y1="8" x2="176" y2="8" stroke="#d7dce2" stroke-width=".5"/>
      <defs>
        <g id="tickOn"><rect width="8" height="6" rx=".5" fill="var(--orange)"/><path d="M2 3 L3.6 4.5 L6.2 1.6" stroke="#fff" stroke-width=".8" fill="none"/></g>
        <g id="tickOff"><rect width="8" height="6" rx=".5" fill="#dadde1"/><path d="M2 3 L3.6 4.5 L6.2 1.6" stroke="#fff" stroke-width=".8" fill="none"/></g>
        <g id="row">
          <text x="0" y="4" font-size="3" font-weight="600" fill="#333" font-family="Open Sans, sans-serif">Lorem Ipsum</text>
          <text x="0" y="8" font-size="2.4" fill="#9aa0a6" font-family="Open Sans, sans-serif">Lorem ipsum dolor</text>
          <use href="#tickOn" x="43" y="1"/><use href="#tickOn" x="65" y="1"/>
          <use href="#tickOff" x="87" y="1"/><use href="#tickOff" x="109" y="1"/><use href="#tickOff" x="131" y="1"/><use href="#tickOff" x="153" y="1"/>
          <line x1="0" y1="13" x2="176" y2="13" stroke="#d7dce2" stroke-width=".5"/>
        </g>
      </defs>
      <use href="#row" y="12"/><use href="#row" y="28"/><use href="#row" y="44"/><use href="#row" y="60"/><use href="#row" y="76"/><use href="#row" y="92"/><use href="#row" y="108"/>
    </svg>
    <p class="itg">AI automated accounting</p>
    <p>Ledgra builds automation in stages on top of its current system to reach full automation. It starts by connecting to all sources of accounting data such as bank accounts, credit cards, webshops or document systems. Based on these data, Ledgra AI creates bookings and generates financial reports and features a chat-like interface that lets users talk to it as a trusted advisor.</p>
    <p class="itg">Blockchain software license or Token-as-a-License (TaaL)</p>
  </div>
  <span class="url">www.quorvex.example</span><span class="pnum">1</span>
</section>

<section class="page c3 r3">
  <div class="hd">Headline <em>&nbsp;Here</em></div>
  <div class="body">
    <p class="itg">AI automated accounting</p>
    <p>Ledgra builds automation in stages on top of its current system to reach full automation thanks to Ledgra AI, which automates every manual task performed by the user.</p>
    <div style="margin-top:5px">
      <div class="list-item"><svg width="16" height="16" viewBox="0 0 16 16"><rect width="16" height="16" fill="var(--navy)"/><circle cx="8" cy="8" r="5" fill="var(--orange)"/><path d="M5.6 8 L7.3 9.6 L10.5 6.3" stroke="#fff" stroke-width="1" fill="none"/></svg><div><h4 style="color:#333">AI automated accounting</h4><p>Ledgra builds automation in stages on top of its current system to reach full automation thanks to Ledgra AI.</p></div></div>
      <div class="list-item"><svg width="16" height="16" viewBox="0 0 16 16"><rect width="16" height="16" fill="var(--navy)"/><circle cx="8" cy="8" r="5" fill="var(--orange)"/><path d="M5.6 8 L7.3 9.6 L10.5 6.3" stroke="#fff" stroke-width="1" fill="none"/></svg><div><h4 style="color:#333">AI automated accounting</h4><p>Ledgra builds automation in stages on top of its current system to reach full automation thanks to Ledgra AI.</p></div></div>
      <div class="list-item"><svg width="16" height="16" viewBox="0 0 16 16"><rect width="16" height="16" fill="var(--navy)"/><circle cx="8" cy="8" r="5" fill="var(--orange)"/><path d="M5.6 8 L7.3 9.6 L10.5 6.3" stroke="#fff" stroke-width="1" fill="none"/></svg><div><h4 style="color:#333">AI automated accounting</h4><p>Ledgra builds automation in stages on top of its current system to reach full automation thanks to Ledgra AI.</p></div></div>
      <div class="list-item"><svg width="16" height="16" viewBox="0 0 16 16"><rect width="16" height="16" fill="var(--navy)"/><circle cx="8" cy="8" r="5" fill="var(--orange)"/><path d="M5.6 8 L7.3 9.6 L10.5 6.3" stroke="#fff" stroke-width="1" fill="none"/></svg><div><h4 style="color:#333">AI automated accounting</h4><p>Ledgra builds automation in stages on top of its current system to reach full automation thanks to Ledgra AI.</p></div></div>
      <div class="list-item"><svg width="16" height="16" viewBox="0 0 16 16"><rect width="16" height="16" fill="var(--navy)"/><circle cx="8" cy="8" r="5" fill="var(--orange)"/><path d="M5.6 8 L7.3 9.6 L10.5 6.3" stroke="#fff" stroke-width="1" fill="none"/></svg><div><h4 style="color:#333">AI automated accounting</h4><p>Ledgra builds automation in stages on top of its current system to reach full automation thanks to Ledgra AI.</p></div></div>
    </div>
    <p class="itg" style="margin-top:4px">AI automated accounting</p>
    <p>Ledgra builds automation in stages on top of its current system to reach full automation. It starts by connecting to all sources of accounting data such as bank accounts, credit cards, webshops or document systems. Based on these data, Ledgra AI creates bookings and generates financial reports and features a chat-like interface that lets users talk to it as a trusted advisor.</p>
    <p class="itg">Blockchain software license or Token-as-a-License (TaaL)</p>
    <p>It is possible to create tokens on blockchain that represent software licenses.</p>
  </div>
  <span class="url">www.quorvex.example</span><span class="pnum">1</span>
</section>

<section class="page c4 r3">
  <div class="hd">Headline <em>&nbsp;Here</em></div>
  <div class="twocol">
    <div>
      <h3>Solution</h3>
      <p class="itg">AI automated accounting</p>
      <p>Ledgra builds automation in stages on top of its current system to reach full automation thanks to Ledgra AI. It starts by connecting to all sources of accounting data such as bank accounts, credit cards, webshops or document systems (Filebay or Nodevault). Based on these data, Ledgra AI creates bookings and generates financial reports, and features a chat-like interface that lets users talk to it as a trusted advisor over time for all their accounting queries.</p>
      <p class="itg">Blockchain software license or Token-as-a-License (TaaL)</p>
      <p>It is possible to create tokens on blockchain that represent software licenses, also known as Token-as-a-License. Ledgra creates TaaL by using the Korvin official wallet which interacts with the Korvin blockchain. Upon purchase, the token holder is free to transfer or sell it on a secondary market built over the blockchain. Ledgra checks the validity of a token against the blockchain, so token holders always have access to the software. This makes distribution easier for software developers and resale easier for owners.</p>
    </div>
    <div>
      <p>software owners. All in all, TaaL has a higher value as a normal software license.</p>
      <h3>Pre-ICO Token sale</h3>
      <p>To realize this vision, Ledgra is launching a pre-ICO in the form of a token sale on the Korvin blockchain. 20,000,000 tokens are available for purchase for a 30-day period. Tokens represent lifelong software licenses, and buyers of 15,000 tokens gain access to both Ledgra accounting and invoicing. Future customers will still have the opportunity to buy monthly subscriptions.</p>
      <h3>Future plans</h3>
      <p>A future ICO is planned between 18 and 24 months after the pre-ICO token sale. This offering will support a fully decentralized, privacy-focused ecosystem of applications where each participant is rewarded.</p>
      <h3>Solution</h3>
      <p class="itg">AI automated accounting</p>
      <p>Ledgra builds automation in stages on top of its current system to reach full automation thanks to Ledgra AI, which automates every manual task.</p>
    </div>
  </div>
  <span class="url">www.quorvex.example</span><span class="pnum">2</span>
</section>

<section class="page c5 r3">
  <div class="back-contact">
    <b>QUORVEX</b>
    <div>
      <p><span class="dot"></span>+61 3 9000 0000</p>
      <p><span class="dot"></span>hello@quorvex.example</p>
      <p><span class="dot"></span>www.quorvex.example</p>
    </div>
    <div>
      <p>12 Bayside Street</p>
      <p>Port Melbourne VIC 3207</p>
    </div>
  </div>
</section>

</div>
</body>
</html>
```